looking for sleek business card to standout from the crowd!

We are a young biotechnology company looking to help you personalize your health through understanding your genetic make up. We need you help in making a clean but sleek business card design using our new logo. The goal? Any time we give our cards out, people say "nice card!" The feel we are going for is "modern-techy". We don't want to come across as an old, giant pharma company, but not trying to be a hipster either.

Target Market(s)

healthcare and biotechnology industry.

Industry/Entity Type

Biotechnology

Contact Information for Business Card

Info to include on the card will be NAME, TITLE, EMAIL, PHONE. The companies website (www.corvalinbio.com) should also be on the card some where. Would like the logo, when printed, to be raised.

Requirements
Must have
• The logo we have attached in the color it is in. Fonts for text should lean toward more professional/tech.
Nice to have
• Prefer white/light color background
Should not have
• cartoons, landscape backgrounds images.

```html
<!DOCTYPE html>
<html lang="en">
<head>
<meta charset="utf-8">
<title>Corvalin – Business Card</title>
<link rel="stylesheet" href="https://fonts.googleapis.com/css2?family=Montserrat:wght@800&family=Open+Sans:ital,wght@0,400;0,600;1,400&display=swap">
<style>
  :root {
    --bg: #ece9e4;
    --card: #ffffff;
    --heading-blue: #1553a8;
    --band-start: #1565b5;
    --band-end: #0a94cf;
    --text-grey: #4a4a4a;
    --white: #ffffff;
  }
  html, body {
    margin: 0;
    width: 1200px;
    height: 1200px;
    overflow: hidden;
    background: var(--bg);
  }
  .card {
    position: absolute;
    left: 100px;
    top: 315px;
    width: 1000px;
    height: 570px;
    background: var(--card);
    border-radius: 30px;
    overflow: hidden;
    box-shadow: 0 10px 30px rgba(0,0,0,0.12);
    font-family: "Open Sans", Arial, sans-serif;
  }
  .card__band {
    position: absolute;
    left: 0;
    bottom: 0;
    width: 1000px;
    height: 120px;
  }
  .brand {
    position: absolute;
    left: 60px;
    top: 82px;
    font-family: "Open Sans", Arial, sans-serif;
    font-weight: 600;
    font-size: 76px;
    letter-spacing: 2px;
    color: var(--text-grey);
    line-height: 1;
  }
  .divider {
    position: absolute;
    left: 0;
    top: 236px;
    width: 700px;
    height: 2px;
    background: var(--heading-blue);
  }
  .person {
    position: absolute;
    left: 712px;
    top: 186px;
  }
  .person__name {
    font-family: "Montserrat", Arial, sans-serif;
    font-weight: 800;
    font-size: 42px;
    color: var(--heading-blue);
    letter-spacing: 1px;
    line-height: 1;
  }
  .person__title {
    margin-top: 16px;
    font-size: 32px;
    color: var(--text-grey);
    line-height: 1;
  }
  .contacts {
    position: absolute;
    left: 50px;
    top: 262px;
    margin: 0;
    padding: 0;
    list-style: none;
  }
  .contacts__item {
    display: flex;
    align-items: center;
    gap: 12px;
    font-size: 28px;
    font-style: italic;
    color: var(--text-grey);
    height: 42px;
  }
  .contacts__icon {
    width: 22px;
    height: 22px;
    flex: none;
  }
  .website {
    position: absolute;
    right: 60px;
    bottom: 30px;
    font-size: 40px;
    font-weight: 600;
    color: var(--white);
    letter-spacing: 0.5px;
  }
</style>
</head>
<body>
  <div class="card">
    <svg class="card__band" viewBox="0 0 1000 120" aria-hidden="true">
      <defs>
        <linearGradient id="bandFill" x1="0" x2="1" y1="0" y2="0">
          <stop offset="0" stop-color="#1565b5"/>
          <stop offset="1" stop-color="#0a94cf"/>
        </linearGradient>
      </defs>
      <polygon points="0,72 380,72 440,8 1000,8 1000,120 0,120" fill="url(#bandFill)"/>
    </svg>

    <div class="brand">CORVALIN</div>

    <div class="divider"></div>

    <div class="person">
      <div class="person__name">JOHN DOE</div>
      <div class="person__title">Director</div>
    </div>

    <ul class="contacts">
      <li class="contacts__item">
        <svg class="contacts__icon" viewBox="0 0 24 24"><path d="M3 8c0-3 4-5 9-5s9 2 9 5l-4 2-2-3H9L7 10 3 8zM6 12h12l2 8H4z" fill="#1553a8"/></svg>
        1-234-567890
      </li>
      <li class="contacts__item">
        <svg class="contacts__icon" viewBox="0 0 24 24"><rect x="2" y="5" width="20" height="14" rx="2" fill="#1553a8"/><path d="M3 6l9 7 9-7" stroke="#fff" stroke-width="2" fill="none"/></svg>
        john.corvalinbio.com
      </li>
      <li class="contacts__item">
        <svg class="contacts__icon" viewBox="0 0 24 24"><path d="M12 2a7 7 0 0 0-7 7c0 5 7 13 7 13s7-8 7-13a7 7 0 0 0-7-7zm0 10a3 3 0 1 1 0-6 3 3 0 0 1 0 6z" fill="#1553a8"/></svg>
        Dummy city, Dummy Country Land
      </li>
    </ul>

    <div class="website">www.corvalinbio.com</div>
  </div>
</body>
</html>
```